Wandkalender Prächtiges Moorhavel
Zielgruppe
Souvenir- und Geschenkartiekl aus Moorhavel
Aufgabenstellung
· Gesucht wird eine Designvorlage für die Gestaltung eines Jahreswandkalenders mit Naturfotos aus der Inselstadt Moorhavel.
· Es muss nur ein Titelblatt und ein Monatsblatt gestaltet werden, die restlichen 11 Monate würden wir adaptieren.
· Das Format des Kalenders beträgt 50 x 70 cm im Hochformat
· Das Monatslayout soll Bilder im Hoch- und im Querformat zulassen
· Als Anlage habe ich einen ersten Entwurf von uns gepackt, der mir aber zu unoriginell bzw. zu konventionell ist.
· Die Zielgruppe ist tendenziell die Generation 50+

```html
<!DOCTYPE html>
<html lang="de">
<head>
<meta charset="utf-8">
<title>Wandkalender Prächtiges Moorhavel 2017</title>
<link href="https://fonts.googleapis.com/css2?family=Montserrat:wght@400;600;700&family=Parisienne&display=swap" rel="stylesheet">
<style>
:root{
  --bg:#96928b;
  --cover-dark:#2c3630;
  --cover-mid:#3d4941;
  --alt-dark:#27302b;
  --plum-top:#6e6469;
  --plum-bottom:#3a2e37;
  --green-top:#7aa94c;
  --green-bottom:#58892c;
  --rose:#c07a82;
  --sage:#a7c183;
  --accent-red:#b8343c;
  --white:#ffffff;
  --grid:#c9c9c9;
  --ink:#2a2a2a;
  --muted:#a0a0a0;
  --sans:'Montserrat',sans-serif;
  --script:'Parisienne',cursive;
}
*{box-sizing:border-box;margin:0;padding:0}
html,body{width:1200px;height:518px;overflow:hidden;background:var(--bg)}
.stage{position:relative;width:1200px;height:518px}
.sheet{position:absolute;overflow:hidden}
.photo{position:absolute}
.ornament{position:absolute;left:50%;transform:translateX(-50%);width:56px;height:14px;border-radius:7px;background:var(--accent-red);opacity:.35}

/* main cover */
.cover{left:56px;top:30px;width:330px;height:460px;background:linear-gradient(180deg,var(--cover-mid),var(--cover-dark))}
.title-script{position:absolute;left:0;right:0;text-align:center;font-family:var(--script);color:var(--accent-red);font-weight:400}
.title-caps{position:absolute;left:0;right:0;text-align:center;font-family:var(--sans);font-weight:700;color:var(--white)}
.cover .title-script{top:42px;font-size:21px}
.cover .title-caps{top:66px;font-size:14px;letter-spacing:4.5px}

.signoff{position:absolute;display:flex;align-items:flex-end;gap:7px;white-space:nowrap}
.brand{font-family:var(--sans);font-weight:600;color:var(--white);line-height:1}
.edition{font-family:var(--sans);color:var(--white);font-weight:700;line-height:1}
.edition .label{display:block;letter-spacing:1.6px}
.edition .year{display:block;letter-spacing:2px;margin-top:1px}

.cover .signoff{right:13px;bottom:10px}
.cover .brand{font-size:12px;margin-bottom:1px}
.cover .edition .label{font-size:5.5px}
.cover .edition .year{font-size:14px}

/* month sheets */
.month{top:61px;width:237px;height:330px}
.month.august{left:411px;background:linear-gradient(180deg,var(--plum-top),var(--plum-bottom))}
.month.april{left:659px;background:linear-gradient(180deg,var(--green-top),var(--green-bottom))}
.month-head{position:absolute;top:14px;left:0;right:0;text-align:center;color:var(--white);font-family:var(--sans)}
.month-name{font-size:8px;font-weight:700;letter-spacing:2.4px}
.month-in{display:flex;align-items:center;justify-content:center;gap:4px;font-size:3px;font-weight:700;margin-top:3px}
.month-in::before,.month-in::after{content:"";width:20px;height:.6px;background:var(--white)}
.month-brand{font-size:8px;font-weight:600;margin-top:5px}
.month .photo{left:6px;top:66px;width:133px;height:189px}
.caption{position:absolute;left:0;right:0;bottom:5px;text-align:center;font-family:var(--sans);font-size:3px;letter-spacing:.3px;color:var(--white)}
.quote{position:absolute;left:144px;top:66px;width:88px;height:189px;color:var(--white);text-align:center;display:flex;flex-direction:column;justify-content:center;align-items:center;padding:0 8px}
.august .quote{background:var(--rose)}
.april .quote{background:var(--sage)}
.quote p{font-family:var(--script);font-size:6px;line-height:8.5px}
.quote .author{font-family:var(--sans);font-size:3.6px;letter-spacing:.6px;margin-top:8px;line-height:4.5px}
.quote .rule{width:34px;height:.5px;background:var(--white);margin-top:10px}
.quote .mark{width:20px;height:5px;border-radius:3px;background:var(--white);opacity:.35;margin-top:10px}

.cal{position:absolute;left:6px;top:260px;width:226px;height:65px;background:var(--white);display:grid;grid-template-columns:28px repeat(7,1fr);grid-template-rows:repeat(6,1fr);font-family:var(--sans);font-size:4.4px;color:var(--ink)}
.cal span{display:flex;align-items:center;justify-content:center;border-right:.5px solid var(--grid);border-bottom:.5px solid var(--grid)}
.cal .day{font-family:var(--script);font-size:5px}
.cal .kw{font-size:2.6px;justify-content:flex-start;padding-left:8px}
.cal .we{font-weight:700}
.cal .off{color:var(--muted)}

/* alternative cover */
.alt{left:906px;top:61px;width:237px;height:330px;background:var(--alt-dark)}
.alt .signoff{left:0;right:0;top:24px;justify-content:center;gap:6px}
.alt .brand{font-size:15px;margin-bottom:1px}
.alt .edition .label{font-size:3.6px}
.alt .edition .year{font-size:9.5px}
.alt-box{position:absolute;left:145px;top:261px;width:88px;height:65px;background:#1f2522}
.alt-box .ornament{width:32px;height:7px}
.alt-box .title-script{top:20px;font-size:10px}
.alt-box .title-caps{top:33px;font-size:7px;letter-spacing:2px}
.note{position:absolute;left:999px;top:416px;font-family:var(--sans);font-size:10px;color:#1e1e1e}
</style>
</head>
<body>
<div class="stage">

  <section class="sheet cover" aria-label="Titelblatt">
    <div class="ornament" style="top:18px"></div>
    <div class="title-script">Prächtiges</div>
    <div class="title-caps">MOORHAVEL</div>
    <div class="ornament" style="top:90px"></div>
    <div class="photo" role="img" aria-label="Fachwerkhaus hinter Bäumen mit Osterglocken auf der Wiese" style="left:7px;top:120px;width:186px;height:296px;background:linear-gradient(180deg,#d9dde0 0%,#a86f55 35%,#6f8a4a 60%,#4f7a2e 100%)"></div>
    <div class="photo" role="img" aria-label="Hauswand mit blühenden roten Rosen" style="left:200px;top:120px;width:122px;height:171px;background:linear-gradient(160deg,#b8684a 0%,#7b2a22 35%,#3f5a2a 100%)"></div>
    <div class="photo" role="img" aria-label="Badehaus am grünen Seeufer mit Trauerweiden" style="left:200px;top:298px;width:122px;height:117px;background:linear-gradient(180deg,#6f9c3c 0%,#4e7a2a 60%,#5f8f3f 100%)"></div>
    <div class="signoff">
      <div class="brand">Moorhavel</div>
      <div class="edition">
        <span class="label">KALENDER</span>
        <span class="year">2017</span>
      </div>
    </div>
  </section>

  <section class="sheet month august" aria-label="Monatsblatt August">
    <header class="month-head">
      <div class="month-name">AUGUST</div>
      <div class="month-in">IN</div>
      <div class="month-brand">Moorhavel</div>
    </header>
    <div class="photo" role="img" aria-label="Holzsteg mit Segelboot am See im rosa Sonnenuntergang" style="background:linear-gradient(180deg,#d9a3bd 0%,#c98fae 45%,#8b7585 70%,#3f3338 100%)">
      <div class="caption">STEG AM MOORHAVELER SEE IM SONNENUNTERGANG</div>
    </div>
    <div class="quote">
      <p>Sommer ist die Zeit, in der es zu heiss ist, um das zu tun, wozu es im Winter zu kalt war.</p>
      <div class="author">HANNES WETTBERG</div>
      <div class="mark" role="img" aria-label="Zierornament"></div>
    </div>
    <div class="cal">
      <span></span><span class="day">Montag</span><span class="day">Dienstag</span><span class="day">Mittwoch</span><span class="day">Donnerstag</span><span class="day">Freitag</span><span class="day">Samstag</span><span class="day">Sonntag</span>
      <span class="kw">KW 31</span><span class="off">31</span><span>1</span><span>2</span><span>3</span><span>4</span><span class="we">5</span><span class="we">6</span>
      <span class="kw">KW 32</span><span>7</span><span>8</span><span>9</span><span>10</span><span>11</span><span class="we">12</span><span class="we">13</span>
      <span class="kw">KW 33</span><span>14</span><span>15</span><span>16</span><span>17</span><span>18</span><span class="we">19</span><span class="we">20</span>
      <span class="kw">KW 34</span><span>21</span><span>22</span><span>23</span><span>24</span><span>25</span><span class="we">26</span><span class="we">27</span>
      <span class="kw">KW 35</span><span>28</span><span>29</span><span>30</span><span>31</span><span class="off">1</span><span class="off we">2</span><span class="off we">3</span>
    </div>
  </section>

  <section class="sheet month april" aria-label="Monatsblatt April">
    <header class="month-head">
      <div class="month-name">APRIL</div>
      <div class="month-in">IN</div>
      <div class="month-brand">Moorhavel</div>
    </header>
    <div class="photo" role="img" aria-label="Backsteindom mit grünem Turm, davor Osterglocken auf der Wiese" style="background:linear-gradient(180deg,#9cc3e6 0%,#b07a5e 30%,#8f8c7a 50%,#6f9a3a 70%,#d8c62a 85%,#4f7a2e 100%)">
      <div class="caption">MOORHAVELER DOM MIT ZUFAHRT</div>
    </div>
    <div class="quote">
      <p>Ein Monat, in dem das Wetter so unzuverlässig ist, dass es manchmal mit den Vorhersagen übereinstimmt.</p>
      <div class="rule"></div>
      <div class="author">KONRAD LEHMSTEDT<br>(*1925), DT. JOURNALIST</div>
    </div>
    <div class="cal">
      <span></span><span class="day">Montag</span><span class="day">Dienstag</span><span class="day">Mittwoch</span><span class="day">Donnerstag</span><span class="day">Freitag</span><span class="day">Samstag</span><span class="day">Sonntag</span>
      <span class="kw">KW 13</span><span class="off">27</span><span>28</span><span>29</span><span>30</span><span>31</span><span class="we">1</span><span class="we">2</span>
      <span class="kw">KW 14</span><span>3</span><span>4</span><span>5</span><span>6</span><span>7</span><span class="we">8</span><span class="we">9</span>
      <span class="kw">KW 15</span><span>10</span><span>11</span><span>12</span><span>13</span><span>14</span><span class="we">15</span><span class="we">16</span>
      <span class="kw">KW 16</span><span>17</span><span>18</span><span>19</span><span>20</span><span>21</span><span class="we">22</span><span class="we">23</span>
      <span class="kw">KW 17</span><span>24</span><span>25</span><span>26</span><span>27</span><span class="off">28</span><span class="we">29</span><span class="we">30</span>
    </div>
  </section>

  <section class="sheet alt" aria-label="Alternatives Titelblatt">
    <div class="signoff">
      <div class="brand">Moorhavel</div>
      <div class="edition">
        <span class="label">KALENDER</span>
        <span class="year">2017</span>
      </div>
    </div>
    <div class="photo" role="img" aria-label="Fachwerkhaus hinter Bäumen mit Osterglocken auf der Wiese" style="left:6px;top:65px;width:133px;height:189px;background:linear-gradient(180deg,#d9dde0 0%,#a86f55 35%,#6f8a4a 60%,#4f7a2e 100%)"></div>
    <div class="photo" role="img" aria-label="Hauswand mit blühenden roten Rosen" style="left:145px;top:65px;width:88px;height:127px;background:linear-gradient(160deg,#b8684a 0%,#7b2a22 35%,#3f5a2a 100%)"></div>
    <div class="photo" role="img" aria-label="Giebelhäuser aus Backstein am Marktplatz" style="left:145px;top:197px;width:88px;height:58px;background:linear-gradient(180deg,#dfe3e6 0%,#a5634c 40%,#7b5444 100%)"></div>
    <div class="photo" role="img" aria-label="Badehaus am grünen Seeufer mit Trauerweiden" style="left:6px;top:261px;width:133px;height:65px;background:linear-gradient(180deg,#6f9c3c 0%,#4e7a2a 60%,#5f8f3f 100%)"></div>
    <div class="alt-box">
      <div class="ornament" style="top:8px"></div>
      <div class="title-script">Prächtiges</div>
      <div class="title-caps">MOORHAVEL</div>
      <div class="ornament" style="top:46px"></div>
    </div>
  </section>

  <div class="note">alternatives Cover</div>
</div>
</body>
</html>
```